Flyer-Design für Buchhaltungsservice
Zielgruppe
Wir bieten Buchhaltungservice und Lohnbuchhaltungsservice an und möchten damit Kleinunternehmen ansprechen!
Aufgabenstellung
Ich habe ein Text zusammengestellt , dieser kann ergänzt oder geändert werden! Bin für Ideen offen! Diesen Text nutze ich aber schon sehr lange! Ich würde vl. noch die Unterschrift mit einfügen als Abspann! Ich bin am überlegen ob ich ein Foto von mir selbst einfüge, aber das alles würde ich gerne durch den Designer als Vorschlag haben. Bitte bei meinem Bild auch ein Ausschnitt verwenden, das Bild ist absolut unbearbeitet! Gerne auch schwarz/weiß!
Die Sterne müssen bei dem Wort dabei stehen und ganz unten findet sich die Erklärung, dies ist rechtlich sehr wichtig!
Es sollte ein Flyer gestaltet werden was später als Postkarte versendet werden kann siehe Anlage von morvadruck datenblatt, bitte so ein Flyer gestalten!

```html
<!DOCTYPE html>
<html lang="de">
<head>
<meta charset="utf-8">
<title>ZAHLWERK GmbH – Postkarte Buchhaltung</title>
<link href="https://fonts.googleapis.com/css2?family=Carlito:ital,wght@0,400;0,700;1,400&display=swap" rel="stylesheet">
<style>
  :root {
    --brand-blue: #1170b8;
    --accent-blue: #1a6cbf;
    --pale-blue: #c4cfeb;
    --text: #2a2a2a;
    --frame: #c9c9c9;
    --paper: #ffffff;
  }
  * { box-sizing: border-box; margin: 0; padding: 0; }
  html, body { width: 1120px; height: 1200px; overflow: hidden; background: var(--paper); }
  body { position: relative; font-family: "Carlito", "Calibri", sans-serif; color: var(--text); }

  .card { position: absolute; left: 69px; width: 982px; height: 527px; border: 1px solid var(--frame); background: var(--paper); overflow: hidden; }
  .card--front { top: 46px; }
  .card--back { top: 618px; }

  .claim-band { position: absolute; left: 0; top: 0; width: 100%; height: 66px; background: var(--brand-blue); color: #fff; font-size: 33px; letter-spacing: 0.5px; display: flex; align-items: center; justify-content: center; word-spacing: 4px; }
  .portrait { position: absolute; left: 0; top: 66px; width: 542px; height: 461px; background: linear-gradient(100deg, #9a9a9a 0%, #d8d8d8 30%, #ececec 55%, #cfa24a 78%, #5a5a5a 100%); }

  .brand-box { position: absolute; left: 278px; top: 66px; width: 214px; height: 96px; background: var(--brand-blue); display: flex; align-items: center; justify-content: center; gap: 10px; color: #fff; font-size: 28px; letter-spacing: 1px; }
  .brand-box .mark, .brand-footer .mark { width: 16px; height: 16px; background: #fff; }

  .service-box { position: absolute; left: 494px; top: 66px; width: 488px; height: 96px; background: var(--pale-blue); text-align: center; }
  .service-box h1 { font-weight: 400; font-size: 36px; color: var(--accent-blue); line-height: 1; margin-top: 8px; }
  .service-box .services { font-size: 19.5px; color: #333; margin-top: 12px; white-space: nowrap; }
  .service-box .note { position: absolute; right: 94px; top: 76px; font-size: 12.5px; font-style: italic; color: #333; }

  .front-copy { position: absolute; left: 563px; top: 170px; width: 400px; }
  .lead { font-style: italic; color: var(--accent-blue); font-size: 21px; line-height: 1.2; }
  .front-copy p { font-size: 15.5px; line-height: 21px; }
  .front-copy .gap-s { margin-top: 21px; }
  .front-copy .gap-xs { margin-top: 9px; }
  .front-copy .lead.mid { margin-top: 12px; }
  .front-copy .lead.end { margin-top: 14px; }

  .back-copy { position: absolute; left: 58px; top: 14px; width: 540px; }
  .back-copy .lead { font-size: 20px; line-height: 25px; }
  .benefits { list-style: none; margin-top: 7px; font-size: 16px; line-height: 21px; }
  .benefits li { position: relative; padding-left: 17px; }
  .benefits li::before { content: ""; position: absolute; left: 2px; top: 8px; width: 5px; height: 5px; border-radius: 50%; background: var(--accent-blue); }
  .back-copy .lead.closing { margin-top: 9px; }

  .greeting { position: absolute; left: 58px; top: 265px; font-size: 16px; }
  .signer { position: absolute; left: 58px; top: 289px; font-size: 20.5px; }
  .signature { position: absolute; left: 250px; top: 240px; width: 130px; height: 72px; background: linear-gradient(90deg, #f4f4f4, #e6e6e6); }
  .footnote { position: absolute; left: 58px; top: 340px; font-size: 8px; color: #444; letter-spacing: -0.2px; white-space: nowrap; }

  .brand-footer { position: absolute; left: 0; top: 354px; width: 603px; height: 105px; background: var(--brand-blue); color: #fff; }
  .brand-footer .logo { position: absolute; left: 12px; top: 0; width: 200px; height: 105px; display: flex; align-items: center; justify-content: center; gap: 8px; font-size: 24px; letter-spacing: 0.5px; }
  .brand-footer address { position: absolute; left: 183px; top: 12px; font-style: normal; font-size: 16.5px; line-height: 21px; }

  .recipient { position: absolute; left: 627px; top: 306px; font-size: 18px; line-height: 24.6px; color: #111; }
</style>
</head>
<body>

<section class="card card--front">
  <div class="claim-band">ZUVERLÄSSIG &nbsp;•&nbsp; DISKRET &nbsp;•&nbsp; PROFESSIONELL</div>
  <div class="portrait" role="img" aria-label="Schwarz-weißes Foto des Buchhalters am Schreibtisch mit goldener Tischlampe"></div>
  <div class="brand-box"><span class="mark"></span><span>ZAHLWERK GmbH</span></div>
  <div class="service-box">
    <h1>Buchhaltung</h1>
    <p class="services">•&nbsp; mit Hol- und Bringservice •&nbsp; lfd. Lohnbuchhaltung</p>
    <span class="note">(auch Baulohn)</span>
  </div>
  <div class="front-copy">
    <h2 class="lead">Mit Sicherheit kennen Sie die Situation:</h2>
    <p class="gap-s">Sie bekommen die Buchhaltungsunterlagen zurück und es fehlt die Zeit diese zu besprechen!</p>
    <p class="gap-xs">Vermissen Sie nicht auch manchmal die persönliche Betreuung?</p>
    <h2 class="lead mid">Dann stellen Sie sich folgende Situation vor:</h2>
    <p class="gap-s">Ihr persönlicher Buchhalter* holt die Unterlagen kostenlos durch einen Kurier bei Ihnen ab,<br>bucht sie und druckt anschließend die entsprechenden betriebswirtschaftlichen Belege aus und<br>Sie bekommen die Auswertungen ausführlich erläutert.</p>
    <h2 class="lead end">Dieser Service ist möglich!</h2>
  </div>
</section>

<section class="card card--back">
  <div class="back-copy">
    <h2 class="lead">Rufen Sie mich noch heute an, um so schnell wie möglich von meinen Leistungen zu profitieren:</h2>
    <ul class="benefits">
      <li>Ein Dienstleister für das Buchen der lfd. Geschäftsvorfälle der Finanzbuchhaltung und lfd. Lohnbuchhaltung</li>
      <li>Immer gleicher Ansprechpartner</li>
      <li>Persönliche und qualifizierte Betreuung</li>
      <li>Hol- und Bringservice</li>
      <li>auch komplett digitale Buchhaltung* möglich</li>
    </ul>
    <h2 class="lead closing">Sie haben endlich eine Buchhalter* als Ansprechpartner, der Sie sofort entlastet.</h2>
  </div>
  <p class="greeting">Mit freundlichen Grüßen</p>
  <p class="signer">Jonas Reiter</p>
  <div class="signature" role="img" aria-label="Handschriftliche Unterschrift"></div>
  <p class="footnote">*Mein Dienstleistungsangebot in der Buchhaltung umfasst ausschließlich das Buchen lfd. Geschäftsvorfälle, die lfd. Lohnabrechnung und das Fertigen der Lohnsteueranmeldung</p>
  <div class="brand-footer">
    <div class="logo"><span class="mark"></span><span>ZAHLWERK</span></div>
    <address>
      ZAHLWERK GmbH<br>
      Ahornweg 18 &nbsp;•&nbsp; 72622 Nürtingen<br>
      Telefon: 0151 / 000 318 42 &nbsp;•&nbsp; Email: info@zahlwerk-buero.de<br>
      www.zahlwerk-buero.de
    </address>
  </div>
  <div class="recipient">FIrma<br>Firma 2<br>Vorname Nachname<br>Straße<br>Ort<br>Land</div>
</section>

</body>
</html>
```